Cedar Hollow Candle Banner Ad for Upcoming holidays

We would like for you to design an ad for Memorial day and Father's Day. For Memorial Day the sale will be 25% OFF select candles and free shipping when you order $50 or more.
For father's day the deal will be get 30% off all candles and free shipping when you order $75 or more.
Please note: These banners will be on our website, they do not require our logo.Banner size: 314 height x 783 width

Industry/Entity Type

Shipping

Requirements
Must have
• Banner size: 314 height x 783 width
Nice to have
• Picture of our starlit candle
Should not have
• Logo

```html
<!DOCTYPE html>
<html lang="en">
<head>
<meta charset="utf-8">
<title>Cedar Hollow Candle – Memorial Day &amp; Father's Day Banner</title>
<link href="https://fonts.googleapis.com/css2?family=Oswald:wght@500;600&family=Lobster&display=swap" rel="stylesheet">
<style>
  :root{
    --teal:#3f7888;
    --teal-deep:#2f6270;
    --teal-ink:#2e6c7c;
    --white:#ffffff;
    --frame-line:#9fc4cc;
    --photo-a:#eef1ef;
    --photo-b:#c9d9d6;
    --photo-c:#7fb7c4;
  }
  *{margin:0;padding:0;box-sizing:border-box;}
  html,body{width:1200px;height:2992px;overflow:hidden;background:var(--teal);}
  .banner{position:relative;width:1200px;height:2992px;background:var(--teal);overflow:hidden;font-family:'Oswald',sans-serif;color:var(--white);}

  .title-badge{position:absolute;left:145px;top:38px;width:917px;height:898px;}
  .title-badge svg{position:absolute;inset:0;}
  .title-text{position:absolute;left:0;right:0;top:190px;text-align:center;font-family:'Lobster',cursive;font-weight:400;color:var(--teal-ink);font-size:162px;line-height:168px;}

  .offer-heading{position:absolute;left:0;right:0;text-align:center;font-weight:600;font-size:118px;line-height:1;letter-spacing:1px;text-transform:uppercase;}
  .offer-heading.memorial{top:1038px;}
  .offer-heading.fathers{top:1655px;}

  .rule{position:absolute;left:69px;width:1062px;height:4px;background:var(--white);top:1165px;}

  .offer-row{position:absolute;left:0;width:1200px;}
  .offer-row.memorial{top:1230px;height:413px;}
  .offer-row.fathers{top:1833px;height:382px;}
  .discount{position:absolute;left:84px;top:50%;transform:translateY(-50%);display:flex;align-items:flex-start;}
  .discount .percent{font-weight:600;font-size:166px;line-height:1;}
  .discount .off{font-weight:500;font-size:60px;line-height:1;margin-left:34px;margin-top:28px;}
  .divider{position:absolute;left:607px;top:0;bottom:0;width:4px;background:var(--white);}
  .terms{position:absolute;left:657px;top:50%;transform:translateY(-50%);font-weight:500;font-size:56px;line-height:74px;text-transform:uppercase;}

  .product-area{position:absolute;left:0;top:2180px;width:1200px;height:780px;}
  .product-area svg{position:absolute;inset:0;}
  .candle-photo{position:absolute;left:19px;top:120px;width:1162px;height:640px;border-radius:20px;background:linear-gradient(90deg,var(--photo-a) 0%,var(--photo-b) 45%,var(--photo-a) 55%,var(--photo-c) 100%);}
  .footer-band{position:absolute;left:0;bottom:0;width:1200px;height:32px;background:var(--teal-deep);}
</style>
</head>
<body>
<main class="banner">
  <div class="title-badge">
    <svg viewBox="0 0 917 898" width="917" height="898" aria-hidden="true">
      <path d="M160 0 H757 Q757 110 870 110 V400 Q917 449 870 498 V788 Q757 788 757 898 H160 Q160 788 47 788 V498 Q0 449 47 400 V110 Q160 110 160 0 Z" fill="var(--white)"/>
      <path d="M180 28 H737 Q742 125 845 132 V410 Q882 449 845 488 V766 Q742 773 737 870 H180 Q175 773 72 766 V488 Q35 449 72 410 V132 Q175 125 180 28 Z" fill="none" stroke="var(--frame-line)" stroke-width="5"/>
    </svg>
    <h1 class="title-text">Happy<br>Father's<br>Day</h1>
  </div>

  <h2 class="offer-heading memorial">For Memorial Day</h2>
  <div class="rule"></div>
  <section class="offer-row memorial">
    <div class="discount"><span class="percent">25%</span><span class="off">OFF</span></div>
    <div class="divider"></div>
    <p class="terms">For selected<br>candles and<br>free shipping<br>when you order<br>$50 or more</p>
  </section>

  <h2 class="offer-heading fathers">For Father's Day</h2>
  <section class="offer-row fathers">
    <div class="discount"><span class="percent">30%</span><span class="off">OFF</span></div>
    <div class="divider"></div>
    <p class="terms">For selected<br>candles and<br>free shipping<br>when you order<br>$75 or more</p>
  </section>

  <div class="product-area">
    <svg viewBox="0 0 1200 780" width="1200" height="780" aria-hidden="true">
      <path d="M0 140 Q260 40 560 70 Q900 100 1200 0 V780 H0 Z" fill="var(--white)"/>
    </svg>
    <div class="candle-photo" role="img" aria-label="Photo of two lit three-wick jar candles with silver lids, one white and one light blue"></div>
  </div>
  <div class="footer-band"></div>
</main>
</body>
</html>
```